Tallow Creek Biologics - Business Card Design

Business Card Brief;
We require a design for a business card template for our business “Tallow Creek Biologics”.
We are a firm that manufacture positive microbial formulations to enhance agricultural legume crops such as lucence, soy beans and faba beans. We also manufacture microbial formulations that aid in composting of waste organic waste to use as a natural fertilizer.
We are seeking a business card design that portrays a clean, professional organisation dedicated to enhancing nature and sustainable farming techniques.
Our website is www.farobiotix.com.au
Here is a link to a drawing of a soybean plant. One of our main products is used to help grow these. I offer it an an example of the type of graphic that might be used on the card, but will leave you to create your own design; https://pictavault.example/482913067/stock-illustration-leafy-sprout-on-a-plain.html
Two cards are required;
--------------------------------------------------------------------
Card #1
Owen T Radley
Executive Chairman
Mobile: 0412 558304
Email: owen@farobiotix.com.au
---------------------------------------------------------------------------
Card #2
Felix R Dunmore
Chief Financial & Operating Officer
Mobile: 0455 284679
Email felix@farobiotix.com.au

Many thanks
Felix Dunmore

Industry/Entity Type

Agriculture

Colors

Designer to choose colors to be used in the design.

Requirements
Must have
• An elegant design that demonstrates our commitment to enhancing nature.

```html
<!DOCTYPE html>
<html lang="en">
<head>
<meta charset="utf-8">
<title>Tallow Creek Biologics – Business Cards</title>
<link rel="stylesheet" href="https://fonts.googleapis.com/css2?family=Raleway:wght@400&family=Lato:wght@700&family=Open+Sans:wght@400&display=swap">
<style>
  :root {
    --backdrop: #676767;
    --card-light: #ffffff;
    --card-dark: #141414;
    --ink: #1a1a1a;
    --ink-soft: #4a4a4a;
    --brand-grey: #3c3c3c;
    --mark: #2a2a2a;
    --rule: #3a3a3a;
    --on-dark: #ffffff;
  }
  * { box-sizing: border-box; margin: 0; padding: 0; }
  html, body { width: 1200px; height: 802px; overflow: hidden; }
  body { background: var(--backdrop); position: relative; }

  .card {
    position: absolute;
    top: 274px;
    width: 442px;
    height: 265px;
  }
  .card--front { left: 136px; background: var(--card-light); }
  .card--back { left: 624px; background: var(--card-dark); }

  .brand {
    position: absolute;
    left: 30px;
    top: 107px;
    display: flex;
    align-items: center;
    gap: 10px;
  }
  .brand__dot {
    width: 44px;
    height: 44px;
    border-radius: 50%;
    background: var(--mark);
    flex: none;
  }
  .brand__name {
    font-family: "Raleway", sans-serif;
    font-weight: 400;
    font-size: 22px;
    line-height: 25px;
    color: var(--brand-grey);
  }

  .divider {
    position: absolute;
    left: 237px;
    top: 71px;
    width: 1.5px;
    height: 124px;
    background: var(--rule);
  }

  .contact {
    position: absolute;
    left: 251px;
    top: 69px;
    font-family: "Open Sans", sans-serif;
    font-size: 13px;
    line-height: 16px;
    color: var(--ink);
  }
  .contact__name {
    font-family: "Lato", sans-serif;
    font-weight: 700;
    font-size: 16px;
    line-height: 18px;
    text-transform: uppercase;
    letter-spacing: -0.2px;
  }
  .contact__role { color: var(--ink); margin-bottom: 8px; }
  .contact__line { display: flex; align-items: center; gap: 3px; }
  .contact__line svg { width: 10px; height: 10px; flex: none; fill: var(--ink); }
  .contact__address { margin-top: 8px; }

  .back-name {
    position: absolute;
    left: 123px;
    top: 88px;
    font-family: "Raleway", sans-serif;
    font-weight: 400;
    font-size: 39px;
    line-height: 42px;
    color: var(--on-dark);
  }
</style>
</head>
<body>
  <section class="card card--front" aria-label="Business card front">
    <div class="brand">
      <span class="brand__dot"></span>
      <div class="brand__name">Tallow Creek<br>Biologics</div>
    </div>
    <div class="divider"></div>
    <div class="contact">
      <div class="contact__name">Owen T Radley</div>
      <div class="contact__role">Executive Chairman</div>
      <div class="contact__line">
        <svg viewBox="0 0 10 10" aria-hidden="true"><path d="M1 3.2C1 2 2 1.5 5 1.5S9 2 9 3.2L7.4 4 6.8 3H3.2L2.6 4Z"/><rect x="2.2" y="4.6" width="5.6" height="4" rx="0.8"/></svg>
        <span>0412 558304</span>
      </div>
      <div class="contact__line">
        <svg viewBox="0 0 10 10" aria-hidden="true"><rect x="1" y="2.2" width="8" height="5.6" rx="0.5"/><path d="M1.4 2.6 5 5.4 8.6 2.6" fill="none" stroke="#fff" stroke-width="0.9"/></svg>
        <span>owen@farobiotix.com.au</span>
      </div>
      <div class="contact__line">
        <svg viewBox="0 0 10 10" aria-hidden="true"><circle cx="5" cy="5" r="4.2"/><path d="M3 3.2 4.6 3 5 4.4 3.8 5.2 4.2 7 3 6Z M6 2.2 7.6 3.4 7 5 6 4Z" fill="#fff"/></svg>
        <span>www.farobiotix.com.au</span>
      </div>
      <div class="contact__address">27 Wattle Row, Corowa<br>NSW 2646 Australia</div>
    </div>
  </section>

  <section class="card card--back" aria-label="Business card back">
    <div class="back-name">Tallow Creek<br>Biologics</div>
  </section>
</body>
</html>
```